Happy Birthday Postcard for law firm for existing clients

Need a postcard that will go out to our current clients on their birthdays. Prefer to have our logo incorporated as part of the design so it reminds them about our business. The back needs to say "Happy Birthday from the team at Dunmore Law Firm."

We are a law firm that services local clients. Needs to be mailed so the backside right half needs to be left blank except the return address (in NEEDS below) so it can be mailed with a mailing label.

Target Market(s)

existing customers, varying age range and demographic profile

Industry/Entity Type

Legal

Font styles to use
Sans Serif
Script

Colors

Designer to choose colors to be used in the design.

Requirements
Must have
• Our logo preferrably on the front (can be modified or added to so it fits a birthday message. And needs to be mailed so the back right side needs to be left open for address labels. The firms return address is
• Dunmore Law Firm
• 4718 W Pebblecrest Ave
• Springfield, MO 65917
• Needs to have the text included in the project description on the back, or some close iteration of it if space is limited.
Nice to have
• Some illustration or graphic on the front with the logo that shows it is a birthday postcard

```html
<!DOCTYPE html>
<html lang="en">
<head>
<meta charset="utf-8">
<title>Dunmore Law Firm – Birthday Postcard</title>
<link href="https://fonts.googleapis.com/css2?family=Great+Vibes&family=Open+Sans:wght@400;600;700&display=swap" rel="stylesheet">
<style>
  :root {
    --page-bg: #ebe7e2;
    --card-white: #ffffff;
    --sky-light: #e4f1f3;
    --sky-mid: #c4dfe3;
    --navy: #2f5a8c;
    --script-blue: #34598c;
    --logo-grey: #77777d;
    --address-name: #6a6aa8;
    --address-grey: #8a8a8e;
    --rule-grey: #d6d6d6;
    --frosting: #f4ecd2;
    --chocolate: #4a3427;
    --candle-blue: #4fb4e0;
  }
  * { margin: 0; padding: 0; box-sizing: border-box; }
  html, body {
    width: 866px; height: 1200px; overflow: hidden;
    background: var(--page-bg);
    font-family: "Open Sans", Arial, sans-serif;
  }
  .postcard {
    position: absolute; left: 97px; width: 697px; height: 497px;
    box-shadow: 0 6px 14px rgba(0,0,0,0.18);
    overflow: hidden;
  }
  .postcard--front {
    top: 66px;
    background: radial-gradient(ellipse at 75% 45%, var(--sky-light) 0%, var(--sky-mid) 85%);
  }
  .postcard--back { top: 626px; background: var(--card-white); }

  .greeting {
    position: absolute; left: 62px; top: 50px;
    font-family: "Great Vibes", cursive;
    font-size: 84px; line-height: 82px;
    color: var(--script-blue);
  }
  .greeting span { display: block; }
  .greeting .line-two { padding-left: 22px; }

  .ribbon {
    position: absolute; left: 38px; top: 279px; width: 342px; height: 45px;
  }
  .ribbon svg { position: absolute; inset: 0; }
  .ribbon-text {
    position: relative; line-height: 45px; text-align: center;
    color: #fff; font-size: 14.5px; font-weight: 400; letter-spacing: 0.2px;
  }

  .firm-mark {
    position: absolute; display: flex; align-items: center; gap: 10px;
    color: var(--logo-grey); font-weight: 400; letter-spacing: 1px;
  }
  .firm-mark .mark-square {
    width: 14px; height: 14px; background: var(--logo-grey); opacity: .55;
  }
  .firm-mark--front { left: 96px; top: 410px; font-size: 26px; }
  .firm-mark--back { left: 50px; top: 84px; font-size: 28px; }

  .cupcake-photo {
    position: absolute; left: 406px; top: 60px; width: 250px; height: 415px;
    border-radius: 40px 40px 18px 18px;
    background: linear-gradient(180deg,
      rgba(79,180,224,0.55) 0%, rgba(79,180,224,0.55) 42%,
      var(--frosting) 50%, var(--frosting) 64%,
      var(--chocolate) 70%, var(--chocolate) 100%);
  }

  .divider {
    position: absolute; left: 347px; top: 50px; width: 1px; height: 375px;
    background: var(--rule-grey);
  }
  .return-address {
    position: absolute; left: 387px; top: 32px;
    font-size: 13px; line-height: 18px; color: var(--address-grey);
  }
  .return-address .firm-name { color: var(--address-name); font-weight: 600; }
  .stamp-box {
    position: absolute; left: 586px; top: 27px; width: 93px; height: 56px;
    border: 1.5px solid var(--rule-grey);
  }
</style>
</head>
<body>
  <section class="postcard postcard--front">
    <h1 class="greeting"><span>Happy</span><span class="line-two">Birthday</span></h1>
    <div class="ribbon">
      <svg width="342" height="45" viewBox="0 0 342 45" aria-hidden="true">
        <polygon points="0,0 342,0 330,22.5 342,45 0,45 12,22.5" fill="var(--navy)"/>
      </svg>
      <p class="ribbon-text">FROM THE TEAM AT DUNMORE LAW FIRM</p>
    </div>
    <div class="firm-mark firm-mark--front"><span class="mark-square"></span>DUNMORE LAW</div>
    <div class="cupcake-photo" role="img" aria-label="Photo of a chocolate cupcake with cream frosting and lit blue polka-dot candles"></div>
  </section>

  <section class="postcard postcard--back">
    <div class="firm-mark firm-mark--back"><span class="mark-square"></span>DUNMORE LAW</div>
    <div class="divider"></div>
    <address class="return-address" style="font-style:normal">
      <div class="firm-name">Dunmore Law Firm</div>
      <div>4718 W Pebblecrest Ave</div>
      <div>Springfield, MO 65917</div>
    </address>
    <div class="stamp-box"></div>
  </section>
</body>
</html>
```